Medical Cannabis company is looking for a LOGO design *

SILVER MERIDIAN (SM) is a new company in the Israeli medical cannabis industry. We will engage in PREMIUM medical cannabis growing and cultivation and also manufacturing of HIGH-END cannabis based medical products.
the design should reflect luxury, high-end and Pharma-grade products.
the design should use color GOLD and NOT using the famous cannabis leaf !

Target Market(s)

international medical cannabis Pharmaceutical companies
and of course local and international patients

Contact Information for Business Card

Ron Ben-Amit
Founder and CEO

Silver Meridian
Medical grade cannabis

ronbenamit@mailpost-example.com
972-52-3186407

Colors
ffc214
fbed22

Requirements
Must have
• clean and simple
• luxury
• gold !!
• (can also have green for Cannabis and/or blue for Pharma)
Should not have
• cannabis leaf

```html
<!DOCTYPE html>
<html lang="en">
<head>
<meta charset="utf-8">
<title>Silver Meridian — Business Card</title>
<link rel="stylesheet" href="https://fonts.googleapis.com/css2?family=Karla:wght@400;500;700&display=swap">
<style>
  :root {
    --gold: #ffc214;
    --gold-deep: #fbb62e;
    --lemon: #fbed22;
    --ink: #4a4a4a;
    --ink-soft: #6b6b6b;
    --rule: #d9d9d9;
    --card: #ffffff;
    --backdrop: #eeeeec;
  }
  * { box-sizing: border-box; margin: 0; padding: 0; }
  html, body {
    width: 1200px;
    height: 1200px;
    overflow: hidden;
    background: var(--backdrop);
    font-family: "Karla", Arial, sans-serif;
  }
  .stage {
    position: relative;
    width: 1200px;
    height: 1200px;
  }
  .card {
    position: absolute;
    left: 180px;
    width: 840px;
    height: 480px;
    background: var(--card);
    box-shadow: 0 2px 10px rgba(0,0,0,0.08);
    overflow: hidden;
  }
  .card-front { top: 90px; }
  .card-back { top: 630px; }

  /* Front */
  .brand {
    position: absolute;
    left: 0; right: 0;
    top: 182px;
    text-align: center;
  }
  .brand-name {
    font-size: 44px;
    font-weight: 700;
    color: var(--gold-deep);
    letter-spacing: 0.5px;
    line-height: 1;
  }
  .brand-tagline {
    margin-top: 14px;
    display: inline-flex;
    align-items: center;
    gap: 14px;
    font-size: 21px;
    font-weight: 400;
    color: var(--ink-soft);
    letter-spacing: 2.5px;
  }
  .brand-tagline::before,
  .brand-tagline::after {
    content: "";
    display: block;
    width: 36px;
    height: 1.5px;
    background: var(--ink-soft);
  }

  /* Back */
  .person {
    position: absolute;
    left: 0;
    width: 420px;
    top: 204px;
    text-align: center;
  }
  .person-name {
    font-size: 31px;
    font-weight: 700;
    color: var(--gold-deep);
    line-height: 1.1;
  }
  .person-title {
    margin-top: 6px;
    font-size: 21px;
    color: var(--ink);
  }
  .divider {
    position: absolute;
    left: 420px;
    top: 164px;
    width: 2px;
    height: 160px;
    background: linear-gradient(to bottom, rgba(217,217,217,0), var(--rule) 25%, var(--rule) 75%, rgba(217,217,217,0));
  }
  .contact {
    position: absolute;
    left: 462px;
    top: 206px;
    list-style: none;
  }
  .contact-item {
    display: flex;
    align-items: center;
    gap: 12px;
    font-size: 19px;
    color: var(--ink);
    height: 40px;
    white-space: nowrap;
  }
  .contact-icon {
    width: 20px;
    height: 20px;
    flex: none;
  }
  .footer-band {
    position: absolute;
    left: 0;
    right: 0;
    bottom: 0;
    height: 116px;
    background: linear-gradient(to bottom, var(--lemon) 0%, var(--gold) 35%, var(--gold-deep) 100%);
  }
</style>
</head>
<body>
<main class="stage">
  <section class="card card-front" aria-label="Business card front">
    <div class="brand">
      <div class="brand-name">Silver Meridian</div>
      <div class="brand-tagline">medical grade cannabis</div>
    </div>
  </section>

  <section class="card card-back" aria-label="Business card back">
    <div class="person">
      <div class="person-name">Ron Ben-Amit</div>
      <div class="person-title">Founder and CEO</div>
    </div>
    <div class="divider"></div>
    <ul class="contact">
      <li class="contact-item">
        <svg class="contact-icon" viewBox="0 0 20 20" aria-hidden="true">
          <rect x="1" y="4" width="18" height="12" fill="var(--gold-deep)"/>
          <path d="M1.5 4.5 L10 11 L18.5 4.5" fill="none" stroke="#fff" stroke-width="1.6"/>
        </svg>
        <span>ronbenamit@mailpost-example.com</span>
      </li>
      <li class="contact-item">
        <svg class="contact-icon" viewBox="0 0 20 20" aria-hidden="true">
          <path d="M5.2 2.5c.6-.4 1.4-.3 1.8.3l1.8 2.7c.4.6.3 1.3-.2 1.8l-1.2 1.1c.9 1.9 2.3 3.4 4.2 4.3l1.1-1.2c.5-.5 1.300-.6 1.8-.2l2.7 1.8c.6.4.7 1.2.3 1.8l-1 1.5c-.6.9-1.7 1.3-2.7 1C8.6 16 4 11.4 2.6 6.2c-.3-1 .1-2.1 1-2.7z" fill="var(--gold-deep)"/>
        </svg>
        <span>972-52-3186407</span>
      </li>
    </ul>
    <div class="footer-band" role="img" aria-label="Decorative gold and yellow band along the bottom edge of the card"></div>
  </section>
</main>
</body>
</html>
```